Brightwell Consulting Business Card Design

Business Card Design for Brightwell Consulting. Brightwell Consulting is a boutique consultancy based in Atlanta, GA., that specializes in marketing strategy, organization planning, and leadership development. We provide solutions for small businesses and startups as well as Summit 400 companies.

http://brightwellconsulting.example/

Target Market(s)

We provide solutions for small businesses and startups as well as Summit 400 companies.

Industry/Entity Type

Consulting

Contact Information for Business Card

Two sided business card with priority on contact information, logo, tag line (Inspiration to Dream More, Do More, Become More)

Colors

Designer to choose colors to be used in the design.

Requirements
Must have
• contact information, logo, tag line (Inspiration to Dream More, Do More, Become More)
• Simple no over communication.
Nice to have
• I would like to see different placements of logo and creative use of both sides of the card
Should not have
• Do not put too much information on the card.

```html
<!DOCTYPE html>
<html lang="en">
<head>
<meta charset="utf-8">
<title>Brightwell Consulting Business Card</title>
<link rel="stylesheet" href="https://fonts.googleapis.com/css2?family=Lato:wght@400;700&display=swap">
<style>
  :root {
    --stage: #2b2b2b;
    --card-dark: #1f1f1f;
    --card-light: #ffffff;
    --ink: #2a2a2a;
    --ink-soft: #555555;
    --band: #333333;
    --band-light: #6e6e6e;
    --rule: #9a9a9a;
    --on-dark: #ffffff;
  }
  * { box-sizing: border-box; margin: 0; padding: 0; }
  html, body { width: 1200px; height: 908px; overflow: hidden; }
  body {
    background: var(--stage);
    font-family: "Lato", sans-serif;
    position: relative;
  }
  .card {
    position: absolute;
    width: 680px;
    height: 388px;
    border-radius: 3px;
    box-shadow: 0 12px 30px rgba(0,0,0,0.45);
    overflow: hidden;
  }
  .card-back {
    left: 120px;
    top: 50px;
    background: var(--card-dark);
  }
  .card-back .brand {
    position: absolute;
    right: 44px;
    bottom: 150px;
    color: var(--on-dark);
    font-weight: 700;
    font-size: 30px;
  }
  .card-front {
    left: 400px;
    top: 470px;
    background: var(--card-light);
  }
  .card-front .brand {
    position: absolute;
    left: 44px;
    top: 118px;
    color: var(--ink);
    font-weight: 700;
    font-size: 34px;
    line-height: 1.15;
    width: 300px;
  }
  .divider {
    position: absolute;
    left: 360px;
    top: 70px;
    width: 1px;
    height: 150px;
    background: var(--rule);
  }
  .contact {
    position: absolute;
    left: 382px;
    top: 66px;
    color: var(--ink);
  }
  .contact .name {
    font-weight: 700;
    font-size: 19px;
    letter-spacing: 0.5px;
  }
  .contact .role {
    font-size: 13px;
    color: var(--ink-soft);
    margin-bottom: 10px;
  }
  .contact ul { list-style: none; }
  .contact li {
    display: flex;
    align-items: center;
    gap: 8px;
    font-size: 15px;
    margin-bottom: 5px;
  }
  .contact svg { width: 18px; height: 18px; flex: none; }
  .tagline-band {
    position: absolute;
    left: 0; right: 0;
    top: 268px;
    height: 36px;
    background: var(--band);
    color: var(--on-dark);
    display: flex;
    align-items: center;
    justify-content: center;
    font-size: 17px;
    letter-spacing: 0.3px;
  }
  .foot-band {
    position: absolute;
    left: 0; right: 0;
    top: 318px;
    height: 18px;
    background: var(--band-light);
  }
</style>
</head>
<body>
  <section class="card card-back" aria-label="Card back">
    <p class="brand">Brightwell Consulting</p>
  </section>

  <section class="card card-front" aria-label="Card front">
    <p class="brand">Brightwell Consulting</p>
    <div class="divider"></div>
    <div class="contact">
      <p class="name">DALE HARMON</p>
      <p class="role">Owner / Manager</p>
      <ul>
        <li>
          <svg viewBox="0 0 18 18" aria-hidden="true"><circle cx="9" cy="9" r="9" fill="#2a2a2a"/><path d="M6 5l2 2-1 1.2c.6 1.2 1.6 2.2 2.8 2.8L11 10l2 2-1.2 1.2C9 13 5 9 4.8 6.2z" fill="#fff"/></svg>
          555-201-3344
        </li>
        <li>
          <svg viewBox="0 0 18 18" aria-hidden="true"><circle cx="9" cy="9" r="9" fill="#2a2a2a"/><rect x="6.2" y="4" width="5.6" height="10" rx="1" fill="none" stroke="#fff" stroke-width="1.2"/><circle cx="9" cy="12.3" r="0.6" fill="#fff"/></svg>
          555-309-6071
        </li>
        <li>
          <svg viewBox="0 0 18 18" aria-hidden="true"><circle cx="9" cy="9" r="9" fill="#2a2a2a"/><rect x="4.5" y="6" width="9" height="6.5" fill="none" stroke="#fff" stroke-width="1.1"/><path d="M4.5 6l4.5 3.6L13.5 6" fill="none" stroke="#fff" stroke-width="1.1"/></svg>
          info@brightwellconsulting.example
        </li>
        <li>
          <svg viewBox="0 0 18 18" aria-hidden="true"><circle cx="9" cy="9" r="9" fill="#2a2a2a"/><g fill="none" stroke="#fff" stroke-width="1"><circle cx="9" cy="9" r="4.8"/><ellipse cx="9" cy="9" rx="2" ry="4.8"/><path d="M4.2 9h9.6M5 6.6h8M5 11.4h8"/></g></svg>
          brightwellconsulting.example
        </li>
      </ul>
    </div>
    <div class="tagline-band">Inspiration to Dream More, Do More, Become More</div>
    <div class="foot-band"></div>
  </section>
</body>
</html>
```